Dorvel519 Smoke shop and Wine Store

DORVEL SMOKE SHOP & WINE INC

Smoke shop, Bill payments, unlock phones,Cellphones, Cellphone accessories and repair.
ADDRESS:
519 Harlow Ave11472Brooklyn, NY
phone # 3470182947
Mobile # 3470264813
E-mail: Dorvel5196@mailbrisk.com
Instagram: DORVELSMOKESHOP

we sell hookah and all hookah accessories and tobaccos. E-cigarettes, vapes, E-juice, vapes parts and replacements, unlocked phones, bill payments and international to-ups,

Target Market(s)

SMOKE sHOPS
Cell phones market

Industry/Entity Type

Shop

Contact Information for Business Card

Tarek Homsi
3470182947
3470264813

Smoke Shop - Unlocked phones - Phone Accessories - phone repair - bill payments - unlock services.

Font styles to use
Decorative

Requirements
Must have
• - attractive colors and designs on the business card.
• - graphics
Nice to have
• Cellphone pics and graphs

```html
<!DOCTYPE html>
<html lang="en">
<head>
<meta charset="utf-8">
<title>Dorvel Smoke Shop &amp; Wine – Business Card</title>
<link href="https://fonts.googleapis.com/css2?family=Arimo:wght@400;700&display=swap" rel="stylesheet">
<style>
  :root {
    --card-black: #070707;
    --stripe-yellow: #ffcc00;
    --stripe-white: #ffffff;
    --text-gold: #f5c818;
    --text-white: #ffffff;
  }
  html, body {
    margin: 0;
    padding: 0;
    width: 1200px;
    height: 686px;
    overflow: hidden;
    background: var(--card-black);
  }
  .card {
    position: relative;
    width: 1200px;
    height: 686px;
    background: var(--card-black);
    font-family: "Arimo", Arial, sans-serif;
    overflow: hidden;
  }
  .card-stripes {
    position: absolute;
    inset: 0;
    width: 1200px;
    height: 686px;
  }
  .brand-name {
    position: absolute;
    top: 78px;
    left: 0;
    width: 1200px;
    text-align: center;
    color: var(--text-gold);
    font-weight: 700;
    font-size: 40px;
    letter-spacing: 2px;
    line-height: 1.2;
    margin: 0;
  }
  .brand-tagline {
    display: block;
    font-size: 27px;
    letter-spacing: 3px;
  }
  .holder-name {
    position: absolute;
    top: 268px;
    left: 0;
    width: 1200px;
    text-align: center;
    color: var(--text-white);
    font-size: 40px;
    font-variant: small-caps;
    margin: 0;
  }
  .name-swoosh {
    position: absolute;
    top: 322px;
    left: 366px;
    width: 468px;
    height: 20px;
  }
  .contact {
    position: absolute;
    top: 379px;
    left: 0;
    width: 1200px;
    text-align: center;
    color: var(--text-gold);
    font-size: 25px;
    line-height: 34px;
    margin: 0;
  }
  .services {
    position: absolute;
    top: 567px;
    left: 0;
    width: 1200px;
    text-align: center;
    color: var(--text-gold);
    font-size: 27px;
    line-height: 35px;
    margin: 0;
  }
</style>
</head>
<body>
<div class="card">
  <svg class="card-stripes" viewBox="0 0 1050 600" preserveAspectRatio="none" aria-hidden="true">
    <polygon fill="var(--stripe-white)" points="0,215 80,600 62,600 0,290"/>
    <polygon fill="var(--stripe-yellow)" points="0,0 14,0 122,600 93,600 0,60"/>
    <polygon fill="var(--stripe-yellow)" points="925,0 950,0 1050,460 1050,560"/>
    <polygon fill="var(--stripe-white)" points="966,0 990,0 1050,250 1050,330"/>
  </svg>

  <h1 class="brand-name">Dorvel<span class="brand-tagline">Smoke Shop &amp; Wine</span></h1>

  <h2 class="holder-name">Tarek Homsi</h2>
  <svg class="name-swoosh" viewBox="0 0 468 20" aria-hidden="true">
    <defs>
      <linearGradient id="swoosh-fade" x1="0" x2="1" y1="0" y2="0">
        <stop offset="0" stop-color="#ffcc00" stop-opacity="0"/>
        <stop offset="0.45" stop-color="#ffcc00" stop-opacity="1"/>
        <stop offset="1" stop-color="#ffcc00" stop-opacity="0"/>
      </linearGradient>
    </defs>
    <path d="M0 10 Q234 2 468 12 Q234 8 0 10 Z" fill="url(#swoosh-fade)"/>
    <path d="M20 10 Q234 4 450 12 L450 13 Q234 10 20 11 Z" fill="url(#swoosh-fade)"/>
  </svg>

  <p class="contact">34701829473470264813<br>519 Harlow Ave11472 Brooklyn,<br>NY3470182947</p>

  <p class="services">Smoke Shop | Bill Payments | Cellphone Accessories<br>Unlock Phones | Cellphones | Repair</p>
</div>
</body>
</html>
```